New Electrical Business advertisement

We Need an A4 flyer created advertising we are a new electrical company servicing this area. We need the flyer to stand out and have a friendly feel to it

Target Market(s)

Home owners and commerical business

Industry/Entity Type

Electrician

Font styles to use
Sans Serif

Requirements
Must have
• must stand out, be eye catching but have a professional feel

Must have company colours orange and blue
RBG Colours
BLUE: R:4 G:116 B:187
ORANGE: R:240 G:86 B:47

```html
<!DOCTYPE html>
<html lang="en">
<head>
<meta charset="utf-8">
<title>Kestrel Electrical Services &amp; Automation – Flyer</title>
<link rel="stylesheet" href="https://fonts.googleapis.com/css2?family=Montserrat:wght@600;700&family=Roboto:ital,wght@0,400;0,700;1,400&family=Roboto+Mono:wght@400;500;700&display=swap">
<style>
  :root {
    --blue: rgb(4,116,187);
    --orange: rgb(240,86,47);
    --orange-dark: #c8432a;
    --red: #e0262e;
    --hex-red: #e8473b;
    --ink: #2b2b2b;
    --text-grey: #555;
    --paper-light: #ececec;
    --paper-dark: #c6c6c9;
    --shadow-grey: #a9a9ad;
    --white: #fff;
  }
  html, body { margin: 0; padding: 0; overflow: hidden; background: #fff; }
  .flyer {
    position: relative; width: 848px; height: 1200px; overflow: hidden;
    font-family: "Roboto", Arial, sans-serif;
    background: linear-gradient(90deg, var(--paper-light) 0%, #e3e3e4 55%, var(--paper-dark) 100%);
  }
  .flyer__art { position: absolute; inset: 0; }
  .abs { position: absolute; margin: 0; }

  .brand-mark {
    left: 166px; width: 200px; top: 452px; text-align: center;
    font-family: "Montserrat", sans-serif; font-weight: 700; font-size: 40px;
    color: var(--blue); letter-spacing: 1px;
  }

  .company { left: 360px; width: 460px; top: 514px; text-align: center; }
  .company__name {
    margin: 0; font-family: "Montserrat", sans-serif; font-weight: 600;
    color: var(--blue); line-height: 0.98; font-size: 66px;
  }
  .company__name span { display: block; }
  .company__name .line-2 { font-size: 72px; }
  .company__tagline {
    margin: 6px 0 0; font-family: "Montserrat", sans-serif; font-weight: 600;
    font-size: 17px; letter-spacing: 10.5px; color: var(--orange); white-space: nowrap;
  }
  .company__acn {
    margin: 6px 0 0; font-family: "Roboto Mono", monospace; font-weight: 500;
    font-size: 20px; color: var(--ink);
  }

  .call { left: 460px; top: 744px; }
  .call__icon { position: absolute; left: 0; top: 7px; }
  .call__label {
    position: absolute; left: 57px; top: 0; white-space: nowrap;
    font-weight: 700; font-size: 19px; color: var(--ink);
  }
  .call__number {
    position: absolute; left: 57px; top: 22px; white-space: nowrap;
    font-family: "Roboto Mono", monospace; font-weight: 500; font-size: 27px; color: var(--orange);
  }

  .emergency {
    left: 440px; width: 400px; top: 820px; text-align: center;
    font-weight: 700; font-size: 21px; letter-spacing: 2px; color: var(--white);
  }

  .contact-person { right: 45px; top: 892px; text-align: right; }
  .contact-person__name {
    margin: 0; font-family: "Roboto Mono", monospace; font-weight: 700;
    font-size: 40px; line-height: 1; color: var(--blue);
  }
  .contact-person__role {
    margin: 4px 0 0; font-family: "Roboto Mono", monospace; font-size: 19px; color: var(--ink);
  }

  .services__title {
    left: 71px; top: 636px; font-weight: 700; font-size: 16px; color: var(--white);
  }
  .services__list {
    left: 38px; top: 684px; width: 260px; padding: 0; list-style: none;
    display: grid; grid-template-columns: 139px 121px; row-gap: 17px;
  }
  .services__list li {
    position: relative; padding-left: 31px; font-style: italic; font-size: 12.5px;
    color: var(--text-grey); line-height: 20px;
  }
  .services__list li::before {
    content: ""; position: absolute; left: 7px; top: 10px; width: 4px; height: 4px;
    border-radius: 50%; background: var(--blue);
  }

  .values__label {
    top: 1010px; width: 120px; text-align: center; font-weight: 700; font-size: 16px; color: var(--red);
  }
  .values__label--safe { left: 9px; }
  .values__label--customer { left: 136px; }
  .values__label--quality { left: 266px; }

  .web-contact {
    right: 153px; font-family: "Roboto Mono", monospace; font-size: 13px; color: var(--white);
    white-space: nowrap;
  }
  .web-contact--site { top: 1115px; }
  .web-contact--mail { top: 1149px; }
</style>
</head>
<body>
<div class="flyer">
  <svg class="flyer__art" width="848" height="1200" viewBox="0 0 848 1200" aria-hidden="false">
    <defs>
      <linearGradient id="photoTone" x1="0" y1="0" x2="1" y2="1">
        <stop offset="0" stop-color="#b9b7b3"/>
        <stop offset="0.45" stop-color="#8a8c91"/>
        <stop offset="1" stop-color="#2f3553"/>
      </linearGradient>
    </defs>

    <!-- header photo area -->
    <polygon points="0,0 848,0 848,298 345,440 0,314" fill="url(#photoTone)"
      role="img" aria-label="Photo of an electrician in work gloves and navy overalls with pliers, coloured wires and an orange hard hat"/>

    <!-- header bands -->
    <polygon points="0,366 175,470 190,455 0,380" fill="var(--shadow-grey)" opacity="0.6"/>
    <polygon points="0,314 185,430 175,470 0,366" fill="var(--orange)"/>
    <polygon points="0,352 178,456 175,470 0,366" fill="var(--orange-dark)"/>
    <polygon points="350,430 848,298 848,345 360,480" fill="var(--orange)"/>
    <polygon points="360,470 848,333 848,345 360,480" fill="var(--orange-dark)"/>
    <polygon points="360,480 848,345 848,356 362,488" fill="var(--shadow-grey)" opacity="0.6"/>

    <!-- logo hexagon -->
    <polygon points="214,383 320,383 364,473 320,563 214,563 166,473"
      fill="#f3f4f8" stroke="var(--hex-red)" stroke-width="5"/>

    <!-- services banner -->
    <polygon points="0,627 274,627 302,663 0,663" fill="var(--blue)"/>

    <!-- phone icon -->
    <path d="M466 752 c-6 4 -7 9 -3 16 c6 12 16 23 28 29 c7 3 12 2 16 -4 l-7 -8 c-3 -2 -5 -1 -8 2 c-8 -4 -15 -11 -19 -19 c3 -3 4 -5 2 -8 z"
      fill="none" stroke="var(--ink)" stroke-width="2.5" stroke-linejoin="round"/>

    <!-- emergency bar -->
    <polygon points="433,856 848,856 848,866 440,866" fill="var(--shadow-grey)"/>
    <polygon points="397,811 848,811 848,856 433,856" fill="var(--orange)"/>
    <polygon points="425,848 848,848 848,856 433,856" fill="var(--orange-dark)"/>

    <!-- value icons -->
    <rect x="35" y="912" width="72" height="76" rx="10" fill="var(--blue)"
      role="img" aria-label="Icon of an electrician wearing a hard hat"/>
    <circle cx="196" cy="950" r="37" fill="var(--blue)"
      role="img" aria-label="Gauge icon"/>
    <rect x="305" y="912" width="38" height="76" rx="12" fill="var(--blue)"
      role="img" aria-label="Energy saving light bulb icon"/>

    <!-- social placeholders -->
    <circle cx="56" cy="1110" r="10" fill="var(--ink)"/>
    <circle cx="97" cy="1110" r="10" fill="var(--ink)"/>
    <circle cx="141" cy="1110" r="10" fill="var(--ink)"/>

    <!-- footer bands -->
    <polygon points="0,1178 698,1012 848,1145 848,1200 0,1200" fill="var(--shadow-grey)"/>
    <polygon points="0,1188 697,1021 848,1168 848,1200 0,1200" fill="var(--blue)"/>
    <polygon points="30,1200 700,1050 838,1200" fill="var(--ink)"/>

    <!-- globe icon -->
    <g fill="none" stroke="var(--white)" stroke-width="1.8">
      <circle cx="717" cy="1124" r="9"/>
      <ellipse cx="717" cy="1124" rx="4" ry="9"/>
      <line x1="708" y1="1124" x2="726" y2="1124"/>
    </g>
    <!-- envelope icon -->
    <g fill="none" stroke="var(--white)" stroke-width="1.8">
      <rect x="708" y="1151" width="19" height="13"/>
      <polyline points="708,1151 717.5,1159 727,1151"/>
    </g>
  </svg>

  <p class="abs brand-mark">KESA</p>

  <div class="abs company">
    <h1 class="company__name"><span>KESTREL</span><span class="line-2">ELECTRICAL</span></h1>
    <p class="company__tagline">SERVICES &amp; AUTOMATION</p>
    <p class="company__acn">ACN: 482 913 507</p>
  </div>

  <div class="abs call">
    <span class="call__label">CALL US NOW</span>
    <span class="call__number">0412 555 038</span>
  </div>

  <p class="abs emergency">24 hs. Emergency Services</p>

  <div class="abs contact-person">
    <p class="contact-person__name">DANIEL MARSH</p>
    <p class="contact-person__role">MANAGING DIRECTOR</p>
  </div>

  <h2 class="abs services__title">OUR SERVICES</h2>
  <ul class="abs services__list">
    <li>Lorem Ipsum</li><li>Lorem Ipsum</li>
    <li>Lorem Ipsum</li><li>Lorem Ipsum</li>
    <li>Lorem Ipsum</li><li>Lorem Ipsum</li>
    <li>Lorem Ipsum</li><li>Lorem Ipsum</li>
  </ul>

  <p class="abs values__label values__label--safe">Safe</p>
  <p class="abs values__label values__label--customer">Customer</p>
  <p class="abs values__label values__label--quality">Quality</p>

  <p class="abs web-contact web-contact--site">kesa-brightpower.com.au</p>
  <p class="abs web-contact web-contact--mail">dan@kesa-brightpower.com.au</p>
</div>
</body>
</html>
```